Business Card Design

Plumbing business.
Looking for a simple but professional looking design.
There are two variations of the logo; white background and black background. The logo with the white background is the primary business logo.
Industry/Entity Type
Business
Contact Information for Business Card
Marcus Fenley
Owner/Licensed Plumber
0412 396 081
info@marcusfenleyplumbing.com.au
www.marcusfenleyplumbing.com.au
Lic. 63941
Look and feel
Each slider illustrates characteristics of the customer's brand and the style your logo design should communicate.

```html
<!DOCTYPE html>
<html lang="en">
<head>
<meta charset="utf-8">
<title>Marcus Fenley Plumbing – Business Card</title>
<link rel="stylesheet" href="https://fonts.googleapis.com/css2?family=Arimo:wght@400&family=Montserrat:wght@500&family=Open+Sans:wght@700&display=swap">
<style>
  :root {
    --ink: #000000;
    --paper: #ffffff;
    --placeholder: #cfcfcf;
  }
  html, body {
    margin: 0;
    padding: 0;
    overflow: hidden;
    background: var(--paper);
  }
  .card {
    position: relative;
    width: 1200px;
    height: 693px;
    background: var(--paper);
    overflow: hidden;
    color: var(--ink);
    font-family: "Arimo", Arial, sans-serif;
  }
  .pipe-illustration {
    position: absolute;
    left: 0;
    top: 0;
  }
  .base-band {
    position: absolute;
    left: 0;
    right: 0;
    top: 572px;
    bottom: 0;
    background: var(--ink);
  }
  .brand-panel {
    position: absolute;
    left: 338px;
    top: 38px;
    width: 550px;
    height: 265px;
    background: var(--ink);
    color: var(--paper);
    font-family: "Montserrat", Arial, sans-serif;
    font-weight: 500;
  }
  .brand-square {
    position: absolute;
    left: 36px;
    top: 34px;
    width: 140px;
    height: 140px;
    background: var(--paper);
  }
  .brand-name {
    position: absolute;
    left: 206px;
    top: 32px;
    margin: 0;
    font-size: 60px;
    line-height: 72px;
    letter-spacing: 0.5px;
    font-weight: 500;
  }
  .brand-trade {
    position: absolute;
    left: 36px;
    right: 20px;
    top: 205px;
    margin: 0;
    font-size: 28px;
    line-height: 32px;
    letter-spacing: 41px;
    font-weight: 500;
  }
  .contact {
    position: absolute;
    margin: 0;
    font-size: 25px;
    line-height: 30px;
    white-space: nowrap;
    letter-spacing: 0.6px;
  }
  .contact-web { left: 406px; top: 321px; }
  .contact-email { left: 253px; top: 470px; }
  .contact-phone { left: 774px; top: 470px; letter-spacing: 2.2px; }
  .licence {
    position: absolute;
    left: 997px;
    top: 597px;
    margin: 0;
    font-family: "Open Sans", Arial, sans-serif;
    font-weight: 700;
    font-size: 23px;
    color: var(--paper);
  }
</style>
</head>
<body>
<main class="card">
  <svg class="pipe-illustration" width="1200" height="693" viewBox="0 0 1200 693" role="img" aria-label="Illustration of a pipe running down the left side and across the card, ending in a dripping outlet">
    <path fill="#cfcfcf" d="M108 0 H156 V360 H1092 V415 H108 Z"/>
    <rect x="1040" y="415" width="52" height="88" fill="#cfcfcf"/>
  </svg>

  <svg class="icons" width="1200" height="693" viewBox="0 0 1200 693" aria-hidden="true" style="position:absolute;left:0;top:0">
    <circle cx="384" cy="331" r="13" fill="none" stroke="#000" stroke-width="3.5"/>
    <line x1="393" y1="341" x2="405" y2="353" stroke="#000" stroke-width="5" stroke-linecap="round"/>
    <rect x="187" y="471" width="55" height="28" fill="#000"/>
    <path d="M188 472 L214.5 489 L241 472 M188 498 L207 484 M241 498 L222 484" fill="none" stroke="#fff" stroke-width="2.5"/>
    <path d="M713 478 Q740 462 768 478 L764 488 L754 486 L753 481 Q740 477 728 481 L727 486 L717 488 Z" fill="#000"/>
    <path d="M728 488 H753 L760 503 H721 Z" fill="#000"/>
    <rect x="735" y="484" width="11" height="7" fill="#000"/>
  </svg>

  <div class="base-band"></div>

  <div class="brand-panel">
    <div class="brand-square"></div>
    <p class="brand-name">MARCUS<br>FENLEY</p>
    <p class="brand-trade">PLUMBING</p>
  </div>

  <p class="contact contact-web">www.marcusfenleyplumbing.com.au</p>
  <p class="contact contact-email">info@marcusfenleyplumbing.com.au</p>
  <p class="contact contact-phone">0-412-396-081</p>
  <p class="licence">Lic. 63941</p>
</main>
</body>
</html>
```